WordPress Website for Pain Relief Clinic

I need a WordPress website designed for my laser pain relief clinic. It needs to be a professional, responsive design with 7 pages: Home, Why Choose Us, Treatable Conditions, Testimonials, FAQ, Franchising, Contact Us. Here is logo: https://s3.cloudvexa-store.net/media.b-r-t-n.net/sitebuilder/361/KelvaroLogoHighQuality.png

Target Market(s)

people with pain,elderly adults,injuries,soreness

Industry/Entity Type

Clinic

Number of Pages Required

5+ page

Colors
0792cd
85abd2

```html
<!DOCTYPE html>
<html lang="en">
<head>
<meta charset="utf-8">
<title>Kelvaro Pain Treatment Center</title>
<link rel="stylesheet" href="https://fonts.googleapis.com/css2?family=Cinzel:wght@400;700&family=Arimo:ital,wght@0,400;0,700;1,400&family=Roboto+Condensed:wght@400&family=Roboto+Slab:wght@300&family=Merriweather:wght@400&display=swap">
<style>
:root{
  --blue:#1367c4;
  --blue-dark:#0d56a8;
  --red:#c8161d;
  --ink:#3a3a3a;
  --muted:#555;
  --rule:#c9c9c9;
  --footer:#343434;
  --footer-text:#f2f2f2;
  --white:#fff;
}
*{margin:0;padding:0;box-sizing:border-box}
html,body{width:675px;height:1200px;overflow:hidden;background:#fff}
body{position:relative;font-family:"Arimo",Arial,sans-serif;color:var(--ink)}
.abs{position:absolute}
/* header */
.brand{left:32px;top:10px}
.brand-name{font-family:"Arimo",sans-serif;font-weight:700;font-size:36px;color:var(--blue);letter-spacing:-1px;line-height:36px}
.brand-tag{font-size:6.5px;letter-spacing:4.6px;color:#333;margin-top:1px}
.book-btn{left:342px;top:26px;width:175px;height:21px;background:var(--red);color:#fff;font-family:"Cinzel",serif;font-size:11px;letter-spacing:.5px;display:flex;align-items:center;justify-content:center}
.call{left:544px;top:24px;display:flex;gap:6px;align-items:center}
.call-label{font-size:10.5px;color:#333}
.call-num{font-size:13px;color:#333}
/* nav */
.nav{left:0;top:64px;width:675px;height:25px;background:var(--blue);display:flex;align-items:center}
.nav a{font-family:"Cinzel",serif;font-size:9.6px;color:#fff;text-decoration:none;padding:0 12.5px;height:25px;display:flex;align-items:center;border-right:1px solid rgba(255,255,255,.25);letter-spacing:.3px}
.nav a.current{color:var(--red)}
.nav a:last-child{border:none}
/* hero */
.hero{left:0;top:89px;width:675px;height:218px;background:linear-gradient(120deg,#e9e9e9 0%,#d5d5d5 40%,#c98d6e 70%,#b9b0aa 100%)}
.hero-title{left:31px;top:272px;font-family:"Cinzel",serif;font-size:25px;color:#fff;text-shadow:0 1px 3px rgba(0,0,0,.5)}
.hours{left:482px;top:253px;width:149px;height:47px;background:#fff;padding:4px 6px;font-size:8px}
.hours h4{font-size:8px;font-weight:400;display:flex;gap:4px;align-items:center;border-bottom:1px dashed var(--rule);padding-bottom:2px;margin-bottom:3px}
.hours p{font-style:italic;line-height:12px}
.arrow{top:178px}
/* band */
.band{left:0;top:307px;width:675px;height:59px;background:var(--blue);color:#fff;font-family:"Merriweather",serif;font-size:11px}
.band-item{top:13px;line-height:14px}
/* about */
.h2{font-family:"Cinzel",serif;color:var(--blue);font-size:15px;border-bottom:1px dashed var(--rule);padding-bottom:2px}
.h2 .big{font-size:20px}
.about{left:38px;top:396px;width:141px}
.about p{font-size:8.2px;line-height:10.9px;margin-top:4px;color:var(--muted)}
.more{font-size:8.5px;color:var(--red)}
.card{top:402px;width:137px}
.card .photo{height:100px;background:linear-gradient(135deg,#d9b59a,#8b6a55)}
.card h3{font-family:"Cinzel",serif;font-weight:400;color:var(--blue);font-size:13px;margin-top:4px;border-bottom:1px dashed var(--rule);padding-bottom:1px}
.card h3 .big{font-size:15px}
.card p{font-size:8.2px;line-height:11.5px;color:var(--muted);margin-top:3px}
.divider{left:38px;top:624px;width:600px;height:1px;background:linear-gradient(90deg,transparent,#ddd 20%,#ddd 80%,transparent)}
/* inquiry */
.sub{font-size:8px;color:#333;margin-top:1px}
.field-label{font-size:8px;font-style:italic;color:#444}
.field{border:1px solid #d4d4d4;background:#fff}
.submit{left:274px;top:848px;width:57px;height:18px;background:var(--red);color:#fff;font-size:12px;display:flex;align-items:center;justify-content:center}
/* reviews */
.pager{top:654px;width:22px;height:22px;background:#333;display:flex;align-items:center;justify-content:center}
.review{left:345px;top:698px;width:292px;height:108px;border:1px solid #e3e3e3;border-radius:6px;padding:9px 14px 0 14px;font-size:7.6px;font-style:italic;line-height:14.8px;color:#444}
.avatar{left:359px;top:795px;width:52px;height:52px;border-radius:50%;background:linear-gradient(#8aa6c4,#5a7ca0);border:3px solid #fff;box-shadow:0 0 3px rgba(0,0,0,.3)}
/* franchise */
.franchise{left:0;top:885px;width:675px;height:127px;background:linear-gradient(135deg,#2f3440,#4d5460 50%,#2a2e36)}
.franchise-text{left:40px;top:898px;width:600px;text-align:center;font-family:"Roboto Condensed",sans-serif;font-weight:400;font-size:12.3px;line-height:22px;color:#fff}
.franchise-btn{left:206px;top:952px;width:240px;height:42px;border:1px solid #fff;padding:3px}
.franchise-btn span{display:flex;height:100%;background:#fff;align-items:center;justify-content:center;font-family:"Roboto Slab",serif;font-weight:300;font-size:19px;color:var(--blue)}
/* footer */
.site-footer{color:var(--footer-text)}
.footer{left:0;top:1012px;width:675px;height:160px;background:var(--footer)}
.f-head{font-family:"Cinzel",serif;font-size:9.5px;color:var(--footer-text);border-bottom:1px solid #555;padding-bottom:5px}
.f-links{list-style:none;font-size:8.2px;line-height:14px;margin-top:6px;color:var(--footer-text)}
.f-links li{display:flex;gap:6px;align-items:center}
.f-contact{font-size:8.2px;line-height:12.5px;margin-top:9px;color:var(--footer-text)}
.f-brand{left:534px;top:1064px;width:108px;text-align:center;font-family:"Cinzel",serif;font-size:18.5px;line-height:22px;color:#9a9a9a}
.map{left:162px;top:1050px;width:192px;height:99px;background:linear-gradient(135deg,#cfe0ec,#e9e4d5 50%,#b9d3e6)}
.copy{left:0;top:1172px;width:675px;height:28px;background:var(--blue);color:#fff;font-size:7.5px;display:flex;align-items:center;justify-content:center}
</style>
</head>
<body>

<header>
  <div class="abs brand">
    <div class="brand-name">Kelvaro</div>
    <div class="brand-tag">PAIN TREATMENT CENTER</div>
  </div>
  <div class="abs book-btn">Book An Appointment</div>
  <div class="abs call">
    <svg width="20" height="20" viewBox="0 0 20 20"><circle cx="10" cy="10" r="9" fill="none" stroke="#1367c4" stroke-width="1.5"/><path d="M7 5c-1 1-1 3 1 6s4 4 5 3l1-1-2-2-1 1c-1 0-3-2-3-3l1-1-2-3z" fill="#1367c4"/></svg>
    <div><div class="call-label">Call Us Today</div><div class="call-num">123-456-7890</div></div>
  </div>
</header>

<nav class="abs nav">
  <a class="current" href="#">Home</a>
  <a href="#">Why Choose Us</a>
  <a href="#">Treatable Conditions</a>
  <a href="#">Testimonials</a>
  <a href="#">FAQ's</a>
  <a href="#">Franchising</a>
  <a href="#">Contact Us</a>
</nav>

<section>
  <div class="abs hero" role="img" aria-label="Clinician applying a handheld laser therapy device to a patient's shoulder"></div>
  <svg class="abs arrow" style="left:10px" width="16" height="24" viewBox="0 0 16 24"><path d="M12 3L4 12l8 9" fill="none" stroke="#fff" stroke-width="3.5"/></svg>
  <svg class="abs arrow" style="left:648px" width="16" height="24" viewBox="0 0 16 24"><path d="M4 3l8 9-8 9" fill="none" stroke="#fff" stroke-width="3.5"/></svg>
  <div class="abs hero-title">Shoulder Pain Laser Therapy</div>
  <div class="abs hours">
    <h4><svg width="10" height="10" viewBox="0 0 10 10"><path d="M1 5l3 4 5-9" fill="none" stroke="#c8161d" stroke-width="1.6"/></svg>WORKING HOURS</h4>
    <p>Monday-Friday 7:00 AM - 5:00 PM<br>Saturday &amp; Sunday Closed</p>
  </div>
</section>

<section class="abs band">
  <div class="abs band-item" style="left:44px;font-weight:700">Check<br>Our Services</div>
  <svg class="abs" style="left:128px;top:14px" width="40" height="32" viewBox="0 0 40 32"><g stroke="#fff" stroke-width="1.5"><path d="M20 16L4 4M20 16L38 14M20 16l-6 14M20 16l12 12M20 16l2-14M20 16L8 22"/></g><circle cx="20" cy="16" r="4" fill="#fff"/></svg>
  <svg class="abs" style="left:170px;top:0" width="30" height="59"><path d="M28 0L2 59" stroke="rgba(255,255,255,.5)"/></svg>
  <div class="abs band-item" style="left:218px">Book An<br>Appointment</div>
  <svg class="abs" style="left:323px;top:15px" width="26" height="28" viewBox="0 0 26 28"><rect x="4" y="6" width="16" height="18" fill="none" stroke="#fff" stroke-width="1.6" transform="rotate(-12 12 15)"/><path d="M8 14l4 4 8-10" fill="none" stroke="#fff" stroke-width="2"/></svg>
  <svg class="abs" style="left:360px;top:0" width="30" height="59"><path d="M28 0L2 59" stroke="rgba(255,255,255,.5)"/></svg>
  <div class="abs band-item" style="left:399px;line-height:16px;top:13px">Contact 123-456-7890<br>Street Name City Name State Zipcode</div>
  <svg class="abs" style="left:617px;top:15px" width="14" height="14" viewBox="0 0 20 20"><circle cx="10" cy="10" r="8.5" fill="none" stroke="#fff" stroke-width="1.5"/><path d="M7 5c-1 1-1 3 1 6s4 4 5 3l1-1-2-2-1 1c-1 0-3-2-3-3l1-1-2-3z" fill="#fff"/></svg>
  <svg class="abs" style="left:620px;top:33px" width="9" height="12" viewBox="0 0 9 12"><path d="M4.5 12L1 5a3.5 3.5 0 117 0z" fill="#fff"/><circle cx="4.5" cy="4.5" r="1.4" fill="#1367c4"/></svg>
</section>

<section>
  <div class="abs about">
    <h2 class="h2"><span class="big">A</span>BOUT <span class="big">U</span>S</h2>
    <p>Lorem ipsum dolor sit am sectetuer adipiscing elit, sed diam nonummy nibh euismod tincidunt ut laoreet dolore magna aliquam eravolutpat. Ut wisi enim ad minim veniam, quis nostrud exerci tation ullam corper suscipit lobortis nisl ut aliqu exreea commodo consequat. Duis autem vel eum iriure dolor facilisi.Lorems is the dummy text.</p>
    <p>Lorem ipsum dolor sit amsectetuer adipiscing elit, sed diam nonummy nibh euismod tincidunt ut laoreet dolore magna aliquam er.</p>
  </div>
  <div class="abs more" style="left:38px;top:595px">Read More &gt;</div>

  <article class="abs card" style="left:194px">
    <div class="photo" role="img" aria-label="Laser treatment on a patient's lower back"></div>
    <h3><span class="big">B</span>ACK <span class="big">P</span>AIN</h3>
    <p>Lorem ipsum dolor sit ame rtetuer readipiscing elit, sed diam lorem onummy nibh euismod tincidunt Lorem ipsum dolor sit ame rtetue aoreet. dolor.</p>
  </article>
  <div class="abs more" style="left:195px;top:595px">Read More &gt;</div>

  <article class="abs card" style="left:345px">
    <div class="photo" role="img" aria-label="Laser device applied to a patient's knee" style="background:linear-gradient(135deg,#6d7f8e,#c9a48a)"></div>
    <h3><span class="big">K</span>NEE <span class="big">P</span>AIN</h3>
    <p>Lorem ipsum dolor sit ame rtetuer readipiscing elit, sed diam lorem onummy nibh euismod tincidunt Lorem ipsum dolor sit ame rtetue aoreet. dolor.</p>
  </article>
  <div class="abs more" style="left:345px;top:595px">Read More &gt;</div>

  <article class="abs card" style="left:495px">
    <div class="photo" role="img" aria-label="Laser device held against a patient's shoulder" style="background:linear-gradient(135deg,#eeeeee,#d6b79c)"></div>
    <h3><span class="big">S</span>HOULDER <span class="big">P</span>AIN</h3>
    <p>Lorem ipsum dolor sit ame rtetuer readipiscing elit, sed diam lorem onummy nibh euismod tincidunt Lorem ipsum dolor sit ame rtetue aoreet. dolor.</p>
  </article>
  <div class="abs more" style="left:495px;top:595px">Read More &gt;</div>

  <div class="abs divider"></div>
</section>

<section>
  <div class="abs" style="left:38px;top:650px;width:293px">
    <h2 class="h2" style="font-size:13px;border:none"><span class="big" style="font-size:16px">Q</span>UICK <span class="big" style="font-size:16px">I</span>NQUIRY</h2>
    <div class="sub" style="margin-top:-2px">Write to us</div>
    <div style="border-bottom:1px dashed var(--rule);margin-top:3px"></div>
  </div>
  <svg class="abs" style="left:310px;top:660px" width="22" height="22" viewBox="0 0 22 22"><path d="M2 12l6 8L21 1" fill="none" stroke="#e9b7b9" stroke-width="2.5"/></svg>

  <div class="abs field-label" style="left:36px;top:695px">First Name*</div>
  <div class="abs field" style="left:36px;top:706px;width:143px;height:25px"></div>
  <div class="abs field-label" style="left:188px;top:695px">Last Name*</div>
  <div class="abs field" style="left:188px;top:706px;width:143px;height:25px"></div>
  <div class="abs field-label" style="left:36px;top:737px">Phone*</div>
  <div class="abs field" style="left:36px;top:748px;width:143px;height:25px"></div>
  <div class="abs field-label" style="left:188px;top:737px">Email*</div>
  <div class="abs field" style="left:188px;top:748px;width:143px;height:25px"></div>
  <div class="abs field-label" style="left:36px;top:779px">Description of a problem*</div>
  <div class="abs field" style="left:36px;top:791px;width:295px;height:49px"></div>
  <div class="abs submit">Submit</div>

  <div class="abs" style="left:345px;top:650px;width:292px">
    <h2 class="h2" style="font-size:13px;border:none"><span class="big" style="font-size:16px">C</span>USTOMER <span class="big" style="font-size:16px">R</span>EVIEWS</h2>
    <div class="sub" style="margin-top:-2px">What other said about us</div>
    <div style="border-bottom:1px dashed var(--rule);margin-top:3px"></div>
  </div>
  <div class="abs pager" style="left:589px"><svg width="8" height="8" viewBox="0 0 8 8"><path d="M5.5 1L2.5 4l3 3" fill="none" stroke="#fff" stroke-width="1.6"/></svg></div>
  <div class="abs pager" style="left:614px"><svg width="8" height="8" viewBox="0 0 8 8"><path d="M2.5 1l3 3-3 3" fill="none" stroke="#fff" stroke-width="1.6"/></svg></div>

  <blockquote class="abs review">
    <span style="font-size:18px;color:#bbb;font-style:normal;line-height:0">&ldquo;</span> Fixed problem with heating system as requested. Performed inspection of car and found other issues that need attention now which we fixed and found other issues to be aware of but did not require immediate attention. (no pressure to have work done which was appreciated) <span style="font-size:18px;color:#bbb;font-style:normal;line-height:0">&rdquo;</span>
  </blockquote>
  <svg class="abs" style="left:448px;top:805px" width="22" height="10"><path d="M1 0l10 9 10-9" fill="#fff" stroke="#e3e3e3"/><path d="M0 0h22" stroke="#fff" stroke-width="2"/></svg>
  <div class="abs avatar" role="img" aria-label="Customer portrait"></div>
  <div class="abs" style="left:424px;top:827px;font-size:9px;color:#222">Mr.Dale Harmon</div>
</section>

<section>
  <div class="abs franchise" role="img" aria-label="Business handshake in a dark office setting"></div>
  <p class="abs franchise-text">Lorem ipsum dolor sit amet, consectetuer adipiscing elit, sed diam nonummy nibh euismod tinciduntLorem ipsum dolor sit amet, consectetuer adipiscing elit, sed diam nonummy nibh.</p>
  <div class="abs franchise-btn"><span>Become Our Franchise</span></div>
</section>

<footer class="site-footer">
  <div class="abs footer"></div>
  <div class="abs" style="left:34px;top:1024px;width:89px">
    <div class="f-head">Quick Links</div>
    <ul class="f-links">
      <li><svg width="4" height="6"><path d="M0 0l4 3-4 3z" fill="#fff"/></svg>Home</li>
      <li><svg width="4" height="6"><path d="M0 0l4 3-4 3z" fill="#fff"/></svg>Why Choose Us</li>
      <li><svg width="4" height="6"><path d="M0 0l4 3-4 3z" fill="#fff"/></svg>Treatable Conditions</li>
      <li><svg width="4" height="6"><path d="M0 0l4 3-4 3z" fill="#fff"/></svg>Testimonials</li>
      <li><svg width="4" height="6"><path d="M0 0l4 3-4 3z" fill="#fff"/></svg>FAQ's</li>
      <li><svg width="4" height="6"><path d="M0 0l4 3-4 3z" fill="#fff"/></svg>Franchising</li>
      <li><svg width="4" height="6"><path d="M0 0l4 3-4 3z" fill="#fff"/></svg>Contact Us</li>
    </ul>
  </div>
  <div class="abs" style="left:143px;top:1035px;width:1px;height:112px;background:#444"></div>
  <div class="abs" style="left:161px;top:1024px;width:193px"><div class="f-head" style="border:none">Our Location</div></div>
  <div class="abs map" role="img" aria-label="Street map showing the clinic location"></div>
  <div class="abs" style="left:372px;top:1035px;width:1px;height:112px;background:#444"></div>
  <div class="abs" style="left:394px;top:1024px;width:120px">
    <div class="f-head" style="border:none">Contact Details</div>
    <div class="f-contact" style="margin-top:6px">Phone<br>123-456-7890</div>
    <div class="f-contact" style="margin-top:6px">Address<br>Street Name City Name<br>State Zipcode</div>
    <div class="f-contact" style="margin-top:6px">Open hours:<br>Monday to Friday 7am-5pm</div>
  </div>
  <div class="abs" style="left:517px;top:1035px;width:1px;height:112px;background:#444"></div>
  <div class="abs f-brand">Kelvaro Laser Pain Relief</div>
  <div class="abs copy">Copyright ©2015. KelvaroLaserPainRelief &nbsp;All Rights Reserved</div>
</footer>

</body>
</html>
```